Brantwell Group needs a business card design

We need a new business card design using the logo recently selected in a logo competition on Pixel Forum. Our business is a consultancy specializing in aviation and energy and the winning business card design will promote an image of precision and professionalism with creativity.

Please use the logo with the name on the front of the card and use a complementary font. Make the back white with either the light grey or dark grey logo.

Target Market(s)

Senior finance and legal leaders at aviation and energy companies

Industry/Entity Type

Management Consulting

Contact Information for Business Card

Peter Haldane
President
Brantwell Group

www.brantwellgroup.example

(555) 304-6198
ph@brantwellgroup.example

Requirements
Must have
• Professional font that goes well with the logo font

```html
<!DOCTYPE html>
<html lang="en">
<head>
<meta charset="utf-8">
<title>Brantwell Group – Business Card</title>
<link rel="stylesheet" href="https://fonts.googleapis.com/css2?family=Montserrat:wght@300;400;500&display=swap">
<style>
  :root {
    --page-bg: #eceff0;
    --card-bg: #e9e9ea;
    --navy: #1b3a6b;
    --dark-grey: #5e5e60;
    --text-grey: #4a4d55;
    --rule: #9a9da4;
  }
  * { box-sizing: border-box; margin: 0; padding: 0; }
  html, body {
    width: 1200px; height: 900px; overflow: hidden;
    background: var(--page-bg);
    font-family: "Montserrat", Arial, sans-serif;
  }
  .sheet {
    width: 1200px; height: 900px;
    display: flex; flex-direction: column;
    align-items: center; justify-content: center; gap: 40px;
  }
  .card {
    position: relative;
    width: 700px; height: 400px;
    background: var(--card-bg);
    box-shadow: 0 2px 6px rgba(0,0,0,0.12);
    overflow: hidden;
  }

  /* Front */
  .card-front .brand {
    position: absolute; right: 56px; top: 56px;
    display: flex; align-items: center; gap: 18px;
  }
  .brand-square { width: 34px; height: 34px; background: var(--navy); }
  .brand-name {
    color: var(--navy); font-weight: 400; text-align: center; line-height: 1;
  }
  .brand-name .word { display: block; font-size: 44px; letter-spacing: 1px; }
  .brand-name .sub { display: block; font-size: 16px; letter-spacing: 22px; margin-top: 10px; margin-right: -22px; }

  .details {
    position: absolute; right: 56px; top: 218px;
    display: flex; align-items: stretch;
  }
  .person {
    text-align: right; padding-right: 18px;
    border-right: 1px solid var(--rule);
    color: var(--text-grey);
  }
  .person-name { color: var(--navy); font-size: 21px; font-weight: 400; letter-spacing: 0.5px; }
  .person-role { font-size: 12px; font-weight: 400; letter-spacing: 1px; margin-top: 6px; text-transform: uppercase; }
  .contact { list-style: none; padding-left: 18px; color: var(--text-grey); }
  .contact li {
    display: flex; align-items: center; gap: 10px;
    font-size: 12.5px; letter-spacing: 0.6px; line-height: 24px;
  }
  .contact svg { width: 14px; height: 14px; flex: none; }
  .band {
    position: absolute; left: 0; right: 0; bottom: 0; height: 24px;
    background: var(--navy);
  }

  /* Back */
  .card-back {
    display: flex; flex-direction: column; align-items: center; justify-content: center; gap: 60px;
  }
  .back-name {
    color: var(--dark-grey); font-weight: 400; font-size: 46px; letter-spacing: 2px;
    display: flex; align-items: center; gap: 18px;
  }
  .back-name .brand-square { background: var(--dark-grey); }
  .back-url {
    color: var(--dark-grey); font-size: 14px; letter-spacing: 9px; text-transform: uppercase;
  }
</style>
</head>
<body>
<main class="sheet">
  <section class="card card-front" aria-label="Card front">
    <div class="brand">
      <span class="brand-square"></span>
      <div class="brand-name">
        <span class="word">BRANTWELL</span>
        <span class="sub">GROUP</span>
      </div>
    </div>

    <div class="details">
      <div class="person">
        <p class="person-name">PETER HALDANE</p>
        <p class="person-role">President</p>
        <p class="person-role">Brantwell Group</p>
      </div>
      <ul class="contact">
        <li>
          <svg viewBox="0 0 16 16" aria-hidden="true"><path fill="#1b3a6b" d="M2 5c0-1.5 2.5-3 6-3s6 1.5 6 3v1.5h-3V5H5v1.5H2z M4 8h8l1.5 6h-11z"/></svg>
          (555) 304-6198
        </li>
        <li>
          <svg viewBox="0 0 16 16" aria-hidden="true"><rect x="1.5" y="3.5" width="13" height="9" fill="none" stroke="#1b3a6b" stroke-width="1.4"/><path d="M1.5 3.5 8 9l6.5-5.5" fill="none" stroke="#1b3a6b" stroke-width="1.4"/></svg>
          ph@brantwellgroup.example
        </li>
        <li>
          <svg viewBox="0 0 16 16" aria-hidden="true"><g fill="none" stroke="#1b3a6b" stroke-width="1.2"><circle cx="8" cy="8" r="6.3"/><ellipse cx="8" cy="8" rx="2.8" ry="6.3"/><path d="M1.7 8h12.6M2.8 4.8h10.4M2.8 11.2h10.4"/></g></svg>
          www.brantwellgroup.example
        </li>
      </ul>
    </div>
    <div class="band"></div>
  </section>

  <section class="card card-back" aria-label="Card back">
    <p class="back-name"><span class="brand-square"></span>BRANTWELL</p>
    <p class="back-url">www.brantwellgroup.example</p>
  </section>
</main>
</body>
</html>
```